TOLVANE WEBSITE

We need a new look for our current website. Tolvane Fast Debt Recovery have been in business since 1977. We want our logo to remain the same however our current website is cluttered and we want something fresh, uncluttered, clean-line and easy to use. Our company colours are red, white and black.
We don't want pictures of people across the top of the page instead, we would like messages to appear (scrolling) across the top on a red background with white writing.
All that is required is from the designer to create a new look home page.
Good afternoon designers,
I have attached another page to the Tolvane Website profile. Could you please take a look and word towards creating something which incorporates the blue box.
I look forward to receiving your designs.
Thanks
Neil

```html
<!DOCTYPE html>
<html lang="en">
<head>
<meta charset="utf-8">
<title>Tolvane Fast Debt Recovery</title>
<link href="https://fonts.googleapis.com/css2?family=Open+Sans:wght@400;600;700;800&family=Oswald:wght@500;700&family=Arimo:wght@400;700&display=swap" rel="stylesheet">
<style>
:root{
  --red:#b93a2b;
  --red-dark:#8f2418;
  --red-text:#c4371f;
  --ink:#1a1a1a;
  --body:#3a3a3a;
  --muted:#8a8a8a;
  --line:#d8d8d8;
  --panel:#f0f0f0;
  --footer:#262626;
  --footer-bottom:#1c1c1c;
  --white:#ffffff;
}
*{box-sizing:border-box;margin:0;padding:0}
html,body{width:966px;height:1200px;overflow:hidden}
body{background:var(--white);font-family:"Open Sans",Arial,sans-serif;color:var(--body);position:relative}
a{color:inherit;text-decoration:none}
.wrap{position:absolute;left:103px;width:761px}

/* header */
.site-header{top:0;height:100px}
.brand{position:absolute;left:0;top:20px;font-family:"Open Sans",sans-serif;font-weight:800;font-size:40px;letter-spacing:-1px;color:var(--ink);display:flex;align-items:center;gap:10px}
.brand .mark{width:14px;height:14px;background:var(--red)}
.social{position:absolute;right:0;top:16px;display:flex;gap:4px}
.social span{width:17px;height:17px;background:#9a9a9a;border-radius:2px}
.phone{position:absolute;right:0;top:54px;font-size:22px;color:var(--ink);display:flex;align-items:center;gap:8px}
.phone svg{width:18px;height:18px}

.main-nav{top:98px;border-top:1px solid #333;height:34px;display:flex;justify-content:space-between;align-items:center;padding-top:8px}
.main-nav a{font-size:14px;color:var(--ink);padding:2px 0;white-space:nowrap}
.main-nav a.active{background:var(--red);color:var(--white);padding:2px 20px 2px 16px}

/* hero */
.hero{top:134px;height:286px;display:flex}
.hero-message{width:329px;height:100%;background:radial-gradient(circle at 40% 40%,#c84a36,#a2301f);color:var(--white);padding:52px 0 0 40px}
.hero-title{display:flex;align-items:center;gap:10px;font-family:"Oswald",sans-serif;text-transform:uppercase}
.hero-title .big{font-size:80px;font-weight:700;color:#3a1410;line-height:.9}
.hero-title .small{font-size:31px;font-weight:700;line-height:1.15}
.hero-message p{font-family:"Arimo",sans-serif;font-size:12px;line-height:1.4;margin-top:14px;width:265px}
.btn-dark{display:inline-block;margin-top:16px;background:linear-gradient(#3a3a3a,#111);color:var(--white);font-size:15px;padding:6px 21px;border-radius:2px}
.hero-photo{flex:1;background:linear-gradient(180deg,#f3f3f3,#d9d9d9 70%,#c2c2c2)}
.slider-arrow{position:absolute;top:244px;width:46px;height:46px;border-radius:50%;background:#cfcfcf;display:flex;align-items:center;justify-content:center}
.slider-arrow.prev{left:43px}
.slider-arrow.next{left:875px}
.slider-arrow svg{width:18px;height:18px}

/* features */
.features{top:442px;height:148px;border:1px solid var(--line);display:flex;padding:14px 0}
.feature{flex:1;padding:0 20px;position:relative;font-family:"Arimo",sans-serif}
.feature+.feature{border-left:1px solid #e6e6e6}
.feature .icon{float:left;width:44px;height:44px;border-radius:50%;border:1px solid #ddd;margin:0 6px 0 0;display:flex;align-items:center;justify-content:center}
.feature h3{font-weight:400;font-size:14px;color:var(--red-text);margin-top:10px;white-space:nowrap}
.feature p{font-size:10px;line-height:1.6;color:var(--body);margin-top:6px}
.feature .btn-red{position:absolute;left:20px;bottom:0;margin:0}
.btn-red{display:inline-block;background:linear-gradient(#c04a36,#8e2516);color:var(--white);font-size:11px;padding:3px 9px;border-radius:2px;margin-top:12px;white-space:nowrap}

/* about */
.about{top:616px;height:328px;background:linear-gradient(180deg,#ececec,#f7f7f7 60%,#f1f1f1)}
.who{position:absolute;left:0;top:0;width:505px;padding:12px 16px;font-family:"Arimo",sans-serif}
.who:after{content:"";position:absolute;right:0;top:10px;height:220px;width:1px;background:linear-gradient(#fff0,#d6d6d6,#fff0)}
.section-title{font-family:"Oswald",sans-serif;font-weight:500;font-size:19px;color:var(--red-text)}
.who .stamp{position:absolute;left:16px;top:54px;width:74px;height:74px;border-radius:50%;background:radial-gradient(circle,#f7f7f7,#e1d8d6);border:1px solid #ddd}
.who h4{font-weight:400;font-size:13px;color:var(--red-text);margin:12px 0 0 88px}
.who p{font-size:9px;line-height:1.7;color:var(--body)}
.who .lead{margin:6px 0 0 88px}
.who .full{margin-top:6px}
.who .full+.full{margin-top:10px}
.quick{position:absolute;left:550px;top:12px;width:200px;height:230px}
.quick ul{list-style:none;margin-top:14px}
.quick li{font-family:"Arimo",sans-serif;font-size:12px;color:var(--body);padding:6px 0 6px 20px;position:relative}
.quick li:before{content:"";position:absolute;left:6px;top:11px;border-left:5px solid var(--red-text);border-top:4px solid transparent;border-bottom:4px solid transparent}
.quick li.highlight{color:var(--red-text)}
.quick .btn-red{position:absolute;right:10px;top:212px;margin:0;font-size:12px;padding:4px 18px}
.offices{position:absolute;left:0;right:0;top:266px;border-top:1px solid #e6c8c2;font-family:"Arimo",sans-serif;font-size:10px;color:var(--body);text-align:center}
.head-office{margin-top:12px;white-space:nowrap}
.head-office b{font-weight:700}
.dot{display:inline-block;width:5px;height:5px;border-radius:50%;background:var(--red-text);margin:0 8px 1px}
.cities{display:flex;justify-content:space-between;padding:0 12px;margin-top:8px;white-space:nowrap}

/* footer */
.site-footer{position:absolute;left:0;top:972px;width:966px;height:185px;background:var(--footer)}
.footer-cols{position:absolute;left:108px;top:18px;display:flex}
.footer-col{width:211px;font-size:9.5px;color:#7a7a7a}
.footer-col h5{font-weight:400;font-size:13px;color:var(--white);margin-bottom:18px}
.footer-col li{list-style:none;margin-bottom:14px;display:flex;align-items:center}
.footer-col li:before{content:"";width:4px;height:4px;border-radius:50%;background:#555;margin-right:8px}
.footer-col li.on{color:var(--white)}
.footer-col.plain li:before{display:none}
.footer-col.plain{width:120px}
.news{display:flex;gap:8px;margin-bottom:14px;font-size:9px}
.news .thumb{width:50px;height:46px;background:linear-gradient(#8d8d8d,#4d4d4d)}
.news strong{display:block;color:var(--white);font-weight:400}
.news span{color:#777}
.news a{display:block;color:var(--white);font-weight:700}
.footer-bottom{position:absolute;left:0;top:1157px;width:966px;height:43px;background:var(--footer-bottom);border-top:1px solid #333;font-family:"Arimo",sans-serif;font-size:8.5px;color:#888;white-space:nowrap}
.footer-links{position:absolute;left:103px;top:17px}
.footer-links a+a:before{content:"|";margin:0 5px;color:#555}
.footer-links a.active{color:var(--white)}
.copyright{position:absolute;right:103px;top:17px}
</style>
</head>
<body>

<header class="wrap site-header">
  <div class="brand"><span>TOLVANE</span><span class="mark"></span></div>
  <div class="social"><span></span><span></span><span></span><span></span></div>
  <div class="phone">
    <svg viewBox="0 0 18 18"><rect width="18" height="18" rx="3" fill="#c4371f"/><path d="M6 4l2 3-1 1.2c.8 1.5 1.7 2.4 3 3L11 10l3 2-1 2c-4 0-8-4-8.5-8.5z" fill="#fff"/></svg>
    1800 555 012
  </div>
</header>

<nav class="wrap main-nav">
  <a class="active" href="#">Home</a>
  <a href="#">About us</a>
  <a href="#">Rates</a>
  <a href="#">Products &amp; Solutions</a>
  <a href="#">Media Centre</a>
  <a href="#">Careers</a>
  <a href="#">Contact us</a>
  <a href="#">Client Login</a>
</nav>

<section class="wrap hero">
  <div class="hero-message">
    <div class="hero-title"><span class="big">NO</span><span class="small">Recovery<br>Charge</span></div>
    <p>Lorem Ipsum is simply dummy text of the printing and typesetting industry. Lorem Ipsum has been the industry's standard dummy.</p>
    <a class="btn-dark" href="#">Read more</a>
  </div>
  <div class="hero-photo" role="img" aria-label="Photo of a smiling business team standing together"></div>
</section>
<a class="slider-arrow prev" href="#" aria-label="Previous"><svg viewBox="0 0 18 18"><path d="M12 2L5 9l7 7" stroke="#fff" stroke-width="3" fill="none"/></svg></a>
<a class="slider-arrow next" href="#" aria-label="Next"><svg viewBox="0 0 18 18"><path d="M6 2l7 7-7 7" stroke="#fff" stroke-width="3" fill="none"/></svg></a>

<section class="wrap features">
  <div class="feature">
    <div class="icon"><svg width="28" height="28" viewBox="0 0 28 28"><circle cx="14" cy="14" r="12" fill="none" stroke="#c4371f" stroke-width="3"/><circle cx="14" cy="14" r="6" fill="none" stroke="#c4371f" stroke-width="3"/><circle cx="14" cy="14" r="2" fill="#c4371f"/></svg></div>
    <h3>Commission rates from 11%</h3>
    <p>and that is all you pay because our service is totally NO RECOVERY - NO CHARGE Lorem ipsum dolor sit amet.</p>
    <a class="btn-red" href="#">Read more</a>
  </div>
  <div class="feature">
    <div class="icon"><svg width="28" height="28" viewBox="0 0 28 28"><path d="M4 14l7 8L25 4" stroke="#c4371f" stroke-width="4" fill="none"/></svg></div>
    <h3>Order Now</h3>
    <p>and that is all you pay because our service is totally NO RECOVERY - NO CHARGE Lorem ipsum dolor sit amet.</p>
    <a class="btn-red" href="#">Read more</a>
  </div>
  <div class="feature">
    <div class="icon"><svg width="28" height="28" viewBox="0 0 28 28"><circle cx="14" cy="14" r="12" fill="none" stroke="#c4371f" stroke-width="3"/><circle cx="14" cy="14" r="6" fill="none" stroke="#c4371f" stroke-width="3"/><circle cx="14" cy="14" r="2" fill="#c4371f"/></svg></div>
    <h3>What we do</h3>
    <p>and that is all you pay because our service is totally NO RECOVERY - NO CHARGE Lorem ipsum dolor sit amet.</p>
    <a class="btn-red" href="#">Read more</a>
  </div>
</section>

<section class="wrap about">
  <div class="who">
    <h2 class="section-title">Who we are</h2>
    <div class="stamp" role="img" aria-label="Illustration of a debt rubber stamp"></div>
    <h4>Debt Collection Specialists</h4>
    <p class="lead">Established in 1977, Tolvane Fast Debt Recovery is Australia's largest privately owned debt collection agency. Pioneering the 'No Recovery - No Charge' service, Tolvane provides quick and easy debt collection solutions. We have developed a reputation of quality and</p>
    <p class="full">Established in 1977, Tolvane Fast Debt Recovery is Australia's largest privately owned debt collection agency. Pioneering the 'No Recovery - No Charge' service, Tolvane provides quick and easy debt collection solutions. We have developed a reputation of quality and client satisfaction through providing a performance based service.</p>
    <p class="full">Lorem ipsum dolor sit amet, consectetur adipiscing elit. Maecenas nec justo quam, id tincidunt dolor. Integer a tellus ut nunc elementum volutpat.</p>
  </div>
  <div class="quick">
    <h2 class="section-title">Quick Links</h2>
    <ul>
      <li class="highlight">Harwell Lawyers</li>
      <li>Submit a Debt</li>
      <li>Corporate Clients</li>
      <li>Small Business</li>
      <li>Make a Payment</li>
      <li>Forms</li>
    </ul>
    <a class="btn-red" href="#">Login here</a>
  </div>
  <div class="offices">
    <div class="head-office"><span class="dot"></span><b>Head office</b> (Melbourne): 14 Linden Road, Mitcham, Victoria, 3132 <span class="dot"></span><b>Tel:</b> 1800 555 012 <span class="dot"></span><b>Fax:</b> (03) 9555 0148</div>
    <div class="cities">
      <span><span class="dot"></span>Adelaide</span><span><span class="dot"></span>Ballarat</span><span><span class="dot"></span>Cairns</span><span><span class="dot"></span>Dubbo</span><span><span class="dot"></span>Geelong</span><span><span class="dot"></span>Launceston</span><span><span class="dot"></span>Newcastle</span><span><span class="dot"></span>Brisbane</span><span><span class="dot"></span>Sydney</span><span><span class="dot"></span>Wagga Wagga</span><span><span class="dot"></span>Warrnambool</span>
    </div>
  </div>
</section>

<footer class="site-footer">
  <div class="footer-cols">
    <div class="footer-col">
      <h5>Latest Newspaper Articles</h5>
      <div class="news"><div class="thumb" role="img" aria-label="Newspaper article photo"></div><div><strong>Overspending, a Xmas denager,</strong><span>Daily Courier - Online, 07/12/2012</span><a href="#">Read more</a></div></div>
      <div class="news"><div class="thumb" role="img" aria-label="Newspaper article photo"></div><div><strong>Overdue bills on the rise,</strong><span>Weekend Chronicle, 02/12/2012</span><a href="#">Read more</a></div></div>
    </div>
    <div class="footer-col">
      <h5>Debt Collection Agency</h5>
      <ul><li class="on">Why Should Choose Tolvane</li><li>Debt Collection Solutions</li><li>Submit Your Debt Online</li><li>Corporate Clients Solutions</li><li>Small Business Solutions</li></ul>
    </div>
    <div class="footer-col">
      <h5>Free Sample &amp; Form</h5>
      <ul><li>Free Sticker System Sample Credit</li><li>Application Form</li><li>Directors' Guarantee Form</li></ul>
    </div>
    <div class="footer-col plain">
      <h5>Contact Tolvane</h5>
      <ul><li>Contact Debt Collection<br>Experts on 1800 555 012</li><li>Enquire Now</li><li>Request a Call Back</li></ul>
    </div>
  </div>
</footer>
<div class="footer-bottom">
  <div class="footer-links"><a class="active" href="#">Home</a><a href="#">Contact Us</a><a href="#">Products &amp; Solutions</a><a href="#">Site Map</a><a href="#">Terms &amp; Conditions</a><a href="#">Privacy</a><a href="#">Disclaimer</a><a href="#">Compliance</a></div>
  <div class="copyright">Copyright © Tolvane Fast Debt Recovery Pty Ltd 2011 All Rights Reserved</div>
</div>

</body>
</html>
```